I need a business card for a new small local scaffolding company. I supply and erect all types of scaffolding for any access need. I thought I could put a safety hat on the Q in KW to emphasize the 'safe' in BOLTHAVEN. Just a thought.

Industry/Entity Type

Safety

Contact Information for Business Card

BOLTHAVEN KW , Tom Varenko , All scaffold & access solutions , Hire , Sales , Transport ,email bolthavenkw@postvane.net , 0438716904, fully accredited , abn 47290831562

```html
<!DOCTYPE html>
<html lang="en">
<head>
<meta charset="utf-8">
<title>BOLTHAVEN KW – Business Card</title>
<link href="https://fonts.googleapis.com/css2?family=Questrial&family=Jura:wght@500&display=swap" rel="stylesheet">
<style>
  :root {
    --backdrop: #e4e4e2;
    --card: #ffffff;
    --card-shade: #eeeeee;
    --accent: #1aa6e8;
    --ink: #2b2b2b;
  }
  * { margin: 0; padding: 0; box-sizing: border-box; }
  html, body { width: 1200px; height: 892px; overflow: hidden; }
  body {
    background: var(--backdrop);
    display: flex;
    flex-direction: column;
    align-items: center;
    justify-content: center;
    gap: 44px;
    font-family: "Questrial", sans-serif;
  }
  .card {
    position: relative;
    width: 640px;
    height: 366px;
    background: linear-gradient(135deg, var(--card) 40%, var(--card-shade));
    box-shadow: 0 6px 18px rgba(0,0,0,.18);
    overflow: hidden;
  }
  .holder { position: absolute; left: 36px; top: 58px; }
  .holder-name { color: var(--accent); font-size: 19px; letter-spacing: .5px; text-transform: uppercase; }
  .holder-title { color: var(--ink); font-size: 14px; letter-spacing: .6px; margin-top: 2px; }
  .services {
    position: absolute; left: 36px; top: 128px;
    font-family: "Jura", sans-serif; font-weight: 500;
    color: var(--ink); font-size: 15px; line-height: 20px;
  }
  .contacts {
    position: absolute; left: 36px; top: 196px;
    list-style: none;
    font-family: "Jura", sans-serif; font-weight: 500;
    color: var(--ink); font-size: 13px;
  }
  .contacts li { display: flex; align-items: center; gap: 8px; height: 22px; }
  .contacts svg { width: 12px; height: 12px; fill: var(--accent); flex: none; }
  .company-name {
    position: absolute; left: 300px; top: 160px;
    color: var(--accent); font-size: 36px; font-weight: 400; letter-spacing: 1.5px;
    white-space: nowrap;
  }
  .band { position: absolute; top: 0; bottom: 0; width: 46px; background: var(--accent); }
  .band-left { left: 70px; }
  .band-right { right: 70px; }
</style>
</head>
<body>
  <section class="card card-front">
    <div class="holder">
      <p class="holder-name">Tom Varenko</p>
      <p class="holder-title">GENERAL MANAGER</p>
    </div>
    <p class="services">All scaffold &amp; access solutions,<br>Hire · Sales · Transport</p>
    <ul class="contacts">
      <li><svg viewBox="0 0 12 12"><path d="M2 1l2 0 1 3-1.5 1a6 6 0 0 0 3.5 3.5L8 7l3 1 0 2c0 1-1 1.5-2 1.5A9 9 0 0 1 .5 3C.5 2 1 1 2 1z"/></svg>0438 716 904</li>
      <li><svg viewBox="0 0 12 12"><path d="M3 0h6v12H3zM4 1.5v8h4v-8z"/></svg>0438716904</li>
      <li><svg viewBox="0 0 12 12"><path d="M1 1h10v10H1zM2.5 3v1h7V3zm0 2.5v1h7v-1zm0 2.5v1h5V8z"/></svg>ABN 47290831562</li>
      <li><svg viewBox="0 0 12 12"><path d="M0 2h12v8H0zM1 3l5 4 5-4v-.2H1z"/></svg>bolthavenkw@postvane.net</li>
      <li><svg viewBox="0 0 12 12"><path d="M6 0a6 6 0 1 0 0 12A6 6 0 0 0 6 0zM5 8.8L2.4 6.2l1-1L5 6.8l3.6-3.6 1 1z"/></svg>Fully accredited</li>
    </ul>
    <h1 class="company-name">BOLTHAVEN KW</h1>
  </section>

  <section class="card card-back">
    <div class="band band-left"></div>
    <div class="band band-right"></div>
  </section>
</body>
</html>
```